Ordnerdesign für Experte für Versicherungs - und Haftungsfragen im Etiketten - und Verpackungsdruck
Ordnerdesign für Experte für Versicherungs - und Haftungsfragen im Etiketten - und Verpackungsdr..
Zielgruppe
Ich bin Henrik Wallmoser Experte für Versicherungs - und Haftungsfragen im Etiketten - und Verpackungsdruck (meine CI Farben sind orange /schwarz ) Meine Company und das Produkt ist die tarvolink und der tarvolnk Schutzbrief für Druckerereien (schwarz/gelb)
Aufgabenstellung
Gesucht wird für mein/unser Projekt : Ordnerdesign PLUS Register eines Notfallhandbuchs für Unternehmer . Es gibt zwei Produktlinien - zu beiden ist jeweils der Farbfächer /Broschüre beigefügt : Entweder der Notfallordner soll unter ' Henrik Wallmoser Experte für Haftungsfragen .. ( Orange Schwarz oder die Farben meiner Company ( tarvolink Schwarz - gelb ) siehe Broschüre angelegt werden. freie Hand , was also besser passt .

```html
<!DOCTYPE html>
<html lang="de">
<head>
<meta charset="utf-8">
<title>tarvolink – Notfallordner</title>
<link rel="stylesheet" href="https://fonts.googleapis.com/css2?family=Manrope:wght@700&display=swap">
<style>
  :root {
    --backdrop: #dedede;
    --folder-yellow: #efc624;
    --pocket-yellow: #d3a900;
    --folder-black: #111111;
    --ink: #161616;
    --paper-white: #f0f0f0;
  }
  html, body {
    margin: 0;
    padding: 0;
    width: 1200px;
    height: 933px;
    overflow: hidden;
    background: var(--backdrop);
  }
  .folder-spread {
    position: absolute;
    left: 130px;
    top: 150px;
    width: 940px;
    height: 633px;
    display: flex;
    gap: 20px;
  }
  .folder-cover {
    position: relative;
    width: 460px;
    height: 633px;
    background: var(--folder-yellow);
    overflow: hidden;
  }
  .brand-name {
    position: absolute;
    left: 30px;
    top: 28px;
    margin: 0;
    font-family: "Manrope", sans-serif;
    font-weight: 700;
    font-size: 15px;
    line-height: 1;
    letter-spacing: 0.01em;
    color: var(--ink);
  }
  .cover-mark {
    position: absolute;
    left: 30px;
    right: 30px;
    bottom: 70px;
    margin: 0;
    font-family: "Manrope", sans-serif;
    font-weight: 700;
    font-size: 78px;
    line-height: 1;
    letter-spacing: -0.02em;
    color: var(--paper-white);
    white-space: nowrap;
  }
  .folder-inside {
    position: relative;
    width: 460px;
    height: 633px;
    background: var(--folder-black);
    overflow: hidden;
  }
  .folder-inside svg {
    position: absolute;
    inset: 0;
    width: 100%;
    height: 100%;
  }
  .pocket-flap { fill: var(--pocket-yellow); }
</style>
</head>
<body>
  <main class="folder-spread">
    <section class="folder-cover" aria-label="Vorderseite des Notfallordners">
      <p class="brand-name">tarvolink®</p>
      <p class="cover-mark">tarvolink</p>
    </section>
    <section class="folder-inside" aria-label="Innenseite mit Einstecktasche">
      <svg viewBox="0 0 460 633" xmlns="http://www.w3.org/2000/svg" aria-hidden="true">
        <path class="pocket-flap" d="M0 300 L250 300 C 370 310, 410 420, 400 633 L0 633 Z"/>
      </svg>
    </section>
  </main>
</body>
</html>
```